Harbor Business Cards

I need a business card designed with the following information.

Company Name: Harbor Wealth Management
Name: BriAnne Dockery
Title: Executive Assistant
Cell: (555) 555-0173
Direct Line: (555) 555-0148
Email: brianne@harborwmx.com
Address: 20537 W. Marlowe PKWY Ste. B
Calderwood, WA 98390

I have attached the logo.
I would like it in navy blue and silver.
Thanks.

```html
<!DOCTYPE html>
<html lang="en">
<head>
<meta charset="utf-8">
<title>Harbor Business Cards</title>
<link rel="stylesheet" href="https://fonts.googleapis.com/css2?family=Noto+Serif:wght@400&family=Marcellus&display=swap">
<style>
  :root {
    --navy: #14264a;
    --navy-deep: #101d3d;
    --silver: #eeeff0;
    --backdrop: #3b3b3d;
    --ink-soft: #2b3550;
    --white: #ffffff;
  }
  * { box-sizing: border-box; margin: 0; padding: 0; }
  html, body {
    width: 1200px;
    height: 755px;
    overflow: hidden;
    background: var(--backdrop);
    font-family: "Noto Serif", Georgia, serif;
  }
  .card {
    position: absolute;
    background: var(--silver);
    overflow: hidden;
  }
  .card-front { left: 88px; top: 217px; width: 498px; height: 288px; }
  .card-back { left: 620px; top: 218px; width: 503px; height: 291px; }

  .brand-block {
    position: absolute;
    left: 0;
    top: 0;
    width: 150px;
    height: 100%;
    background: var(--navy);
  }

  .person-name {
    position: absolute;
    left: 224px;
    top: 104px;
    font-size: 26px;
    line-height: 34px;
    color: var(--navy);
    font-weight: 400;
    white-space: nowrap;
  }
  .person-title {
    position: absolute;
    left: 225px;
    top: 146px;
    font-size: 15px;
    letter-spacing: 2px;
    color: var(--ink-soft);
    white-space: nowrap;
  }
  .contact-list {
    position: absolute;
    left: 224px;
    top: 185px;
    list-style: none;
  }
  .contact-item {
    display: flex;
    align-items: center;
    height: 27px;
    font-size: 18px;
    color: var(--navy);
    white-space: nowrap;
  }
  .contact-icon {
    width: 16px;
    height: 16px;
    margin-right: 14px;
    fill: var(--navy);
    flex: none;
  }

  .company-name {
    position: absolute;
    left: 0;
    width: 100%;
    top: 168px;
    text-align: center;
    font-family: "Marcellus", "Noto Serif", serif;
    color: var(--navy);
    text-transform: uppercase;
  }
  .company-name .word-main {
    display: block;
    font-size: 30px;
    letter-spacing: 9px;
    line-height: 34px;
  }
  .company-name .word-sub {
    display: block;
    margin-top: 6px;
    font-size: 11px;
    letter-spacing: 3px;
  }
  .address-band {
    position: absolute;
    left: 0;
    bottom: 0;
    width: 100%;
    height: 49px;
    background: var(--navy-deep);
    color: var(--white);
    font-size: 13px;
    letter-spacing: 2px;
    display: flex;
    align-items: center;
    justify-content: center;
    white-space: nowrap;
  }
</style>
</head>
<body>
  <section class="card card-front">
    <div class="brand-block" role="img" aria-label="Harbor Wealth Management brand graphic"></div>
    <h1 class="person-name">BriAnne Dockery</h1>
    <p class="person-title">Executive Assistant</p>
    <ul class="contact-list">
      <li class="contact-item">
        <svg class="contact-icon" viewBox="0 0 16 16" aria-hidden="true"><path d="M4 0h8a1 1 0 0 1 1 1v14a1 1 0 0 1-1 1H4a1 1 0 0 1-1-1V1a1 1 0 0 1 1-1zm.5 2v10h7V2zm3.5 11a1 1 0 1 0 0 2 1 1 0 0 0 0-2z"/></svg>
        (555) 555-0173
      </li>
      <li class="contact-item">
        <svg class="contact-icon" viewBox="0 0 16 16" aria-hidden="true"><path d="M1 5c0-2 3-3 7-3s7 1 7 3v1h-4V4.5H5V6H1zM4 7h8l2 3v4H2v-4zm4 1.5a2 2 0 1 0 0 4 2 2 0 0 0 0-4z"/></svg>
        (555) 555-0148
      </li>
      <li class="contact-item">
        <svg class="contact-icon" viewBox="0 0 16 16" aria-hidden="true"><path d="M1 3h14v1.2L8 9 1 4.2zm0 2.6 7 4.8 7-4.8V13H1z"/></svg>
        brianne@harborwmx.com
      </li>
    </ul>
  </section>

  <section class="card card-back">
    <p class="company-name">
      <span class="word-main">Harbor</span>
      <span class="word-sub">Wealth Management</span>
    </p>
    <p class="address-band">20537 W. Marlowe PKWY Ste. B, Calderwood, WA 98390</p>
  </section>
</body>
</html>
```